Need a flyer overhaul and minor changes

flyer is 5.5" x 8.5" we need to change the $250.00 to $325.00, update our company logo on the brochure, and also have an area where we can have the store address (318 W Harlan Ave, Del Rio, TX 78840 - (830) 642-9158). I've attached a our current brochure and our updated logo and we just want to make look better and updated.

Industry/Entity Type

Lending and Finance

Requirements
Nice to have
• updated layout and pictures

```html
<!DOCTYPE html>
<html lang="en">
<head>
<meta charset="utf-8">
<title>Title Loan Comparison Flyer</title>
<link href="https://fonts.googleapis.com/css2?family=Montserrat:wght@400;600;700;800&display=swap" rel="stylesheet">
<style>
  :root{
    --red:#c1272d;
    --green:#215434;
    --ink:#231f20;
    --text:#3a3a3a;
    --white:#ffffff;
    --panel-bg:#eeeeee;
    --blush:#e8c9cc;
  }
  *{box-sizing:border-box;margin:0;padding:0}
  html,body{width:1200px;height:1200px;overflow:hidden;background:#000;font-family:"Montserrat",sans-serif}
  .flyer{position:absolute;left:276px;top:99px;width:648px;height:1001px;overflow:hidden;
    background:radial-gradient(circle at 70% 45%, #f7f2f2 0%, var(--panel-bg) 45%, var(--blush) 130%)}
  .arc{position:absolute;left:0;top:0;width:648px;height:1001px}
  .headline{position:absolute;left:0;width:100%;text-align:center;color:var(--white)}
  .headline--lead{top:22px;font-size:58px;font-weight:400;letter-spacing:1px}
  .headline--main{top:88px;font-size:80px;font-weight:800;letter-spacing:1px}
  .photo{position:absolute;left:0;top:300px;width:302px;height:670px;
    background:linear-gradient(180deg,#6b5246 0%,#d9b49c 28%,#e7edf3 55%,#dfe6ec 100%);
    opacity:.9}
  .offer-amount{position:absolute;left:300px;width:314px;top:240px;text-align:center;color:var(--red);font-weight:800;font-size:44px}
  .offer-label{position:absolute;left:300px;width:314px;top:296px;text-align:center;color:var(--ink);font-weight:700;font-size:24px;letter-spacing:.5px}
  .table{position:absolute;left:299px;top:333px;width:312px;height:387px;border:2.5px solid var(--ink);border-radius:12px;background:var(--white)}
  .col-head{position:absolute;top:0;height:78px;display:flex;align-items:center;justify-content:center;text-align:center}
  .col-head--lender{left:13px;width:138px;color:var(--green);font-weight:600;font-size:17px;line-height:1.15}
  .col-head--title{left:157px;width:138px;color:var(--red);font-weight:800;font-size:21px;line-height:1.15}
  .col{position:absolute;top:76px;width:138px;height:302px;padding-top:9px;color:var(--white)}
  .col--lender{left:13px;background:var(--green)}
  .col--title{left:157px;background:var(--red)}
  .row{display:flex;height:24.5px;align-items:center;font-size:16px}
  .row .n{width:34px;padding-left:12px}
  .col--lender .row .v{font-weight:400}
  .col--title .row .v{font-weight:700}
  .result{position:absolute;top:723px;width:138px;height:62px;color:var(--white);font-weight:700;font-size:19px;text-align:center;padding-top:7px;line-height:1.25}
  .result--lender{left:314px;background:var(--green)}
  .result--title{left:458px;background:var(--red)}
  .pill{position:absolute;left:308px;top:795px;width:295px;height:35px;border-radius:18px;background:var(--ink);color:var(--white);font-weight:700;font-size:22px;text-align:center;line-height:35px;letter-spacing:.5px}
  .brand{position:absolute;left:110px;top:905px;width:210px;color:var(--green);font-weight:600;font-size:26px;line-height:1.1;text-align:center}
  .contact{position:absolute;left:330px;top:906px;color:var(--text);font-size:14.5px}
  .contact li{list-style:none;display:flex;align-items:flex-start;margin-bottom:5px;line-height:1.15}
  .contact svg{flex:none;width:13px;height:13px;margin:1px 8px 0 0}
</style>
</head>
<body>
<div class="flyer">
  <svg class="arc" viewBox="0 0 648 1001" aria-hidden="true">
    <path d="M0,0 H648 V317 Q324,81 0,317 Z" fill="var(--green)"/>
    <path d="M0,0 H648 V305 Q324,69 0,305 Z" fill="var(--red)"/>
  </svg>

  <div class="headline headline--lead">Stuck in a</div>
  <div class="headline headline--main">TITLE LOAN?</div>

  <div class="photo" role="img" aria-label="Smiling woman counting a stack of cash"></div>

  <svg class="arc" viewBox="0 0 648 1001" aria-hidden="true">
    <path d="M0,969 Q324,713 648,969 V1001 H0 Z" fill="var(--green)"/>
    <path d="M0,983 Q324,729 648,983 V1001 H0 Z" fill="var(--white)"/>
    <rect x="0" y="995" width="648" height="6" fill="var(--red)"/>
  </svg>

  <div class="offer-amount">$1,000</div>
  <div class="offer-label">LOAN COMPARISON</div>

  <div class="table">
    <div class="col-head col-head--lender">Crestline<br>Lending</div>
    <div class="col-head col-head--title">TITLE<br>LOAN?</div>
    <div class="col col--lender">
      <div class="row"><span class="n">1</span><span class="v">$131.67</span></div>
      <div class="row"><span class="n">2</span><span class="v">$131.67</span></div>
      <div class="row"><span class="n">3</span><span class="v">$131.67</span></div>
      <div class="row"><span class="n">4</span><span class="v">$131.67</span></div>
      <div class="row"><span class="n">5</span><span class="v">$131.67</span></div>
      <div class="row"><span class="n">6</span><span class="v">$131.67</span></div>
      <div class="row"><span class="n">7</span><span class="v">$131.67</span></div>
      <div class="row"><span class="n">8</span><span class="v">$131.67</span></div>
      <div class="row"><span class="n">9</span><span class="v">$131.67</span></div>
      <div class="row"><span class="n">10</span><span class="v">$131.67</span></div>
      <div class="row"><span class="n">11</span><span class="v">$131.67</span></div>
      <div class="row"><span class="n">12</span><span class="v">$131.67</span></div>
    </div>
    <div class="col col--title">
      <div class="row"><span class="n">1</span><span class="v">$325.00</span></div>
      <div class="row"><span class="n">2</span><span class="v">$325.00</span></div>
      <div class="row"><span class="n">3</span><span class="v">$325.00</span></div>
      <div class="row"><span class="n">4</span><span class="v">$325.00</span></div>
      <div class="row"><span class="n">5</span><span class="v">$325.00</span></div>
      <div class="row"><span class="n">6</span><span class="v">$325.00</span></div>
      <div class="row"><span class="n">7</span><span class="v">$325.00</span></div>
      <div class="row"><span class="n">8</span><span class="v">$325.00</span></div>
      <div class="row"><span class="n">9</span><span class="v">$325.00</span></div>
      <div class="row"><span class="n">10</span><span class="v">$325.00</span></div>
      <div class="row"><span class="n">11</span><span class="v">$325.00</span></div>
      <div class="row"><span class="n">12</span><span class="v">$325.00</span></div>
    </div>
  </div>

  <div class="result result--lender">PAID OFF</div>
  <div class="result result--title">STILL OWE<br>$1,000</div>

  <div class="pill">SE HABLA ESPAÑOL</div>

  <div class="brand">Crestline<br>Lending Group</div>

  <ul class="contact">
    <li>
      <svg viewBox="0 0 14 14"><circle cx="7" cy="7" r="7" fill="var(--red)"/><path d="M7 3.2a2.4 2.4 0 0 0-2.4 2.4C4.6 7.5 7 10.6 7 10.6s2.4-3.1 2.4-5A2.4 2.4 0 0 0 7 3.2z" fill="#fff"/><circle cx="7" cy="5.6" r="0.9" fill="var(--red)"/></svg>
      <span>318 W Harlan Ave, Del Rio,<br>TX 78840</span>
    </li>
    <li>
      <svg viewBox="0 0 14 14"><circle cx="7" cy="7" r="7" fill="var(--red)"/><path d="M4.6 3.6l1.3-.2.7 1.8-.9.7a5 5 0 0 0 2.4 2.4l.7-.9 1.8.7-.2 1.3c-3.3.3-6.1-2.5-5.8-5.8z" fill="#fff"/></svg>
      <span>(830) 642-9158</span>
    </li>
    <li>
      <svg viewBox="0 0 14 14"><circle cx="7" cy="7" r="7" fill="var(--red)"/><circle cx="7" cy="7" r="3.6" fill="none" stroke="#fff" stroke-width="1"/><path d="M3.4 7h7.2M7 3.4c-1.6 2.2-1.6 5 0 7.2M7 3.4c1.6 2.2 1.6 5 0 7.2" fill="none" stroke="#fff" stroke-width=".8"/></svg>
      <span>crestlinelending.com</span>
    </li>
  </ul>
</div>
</body>
</html>
```